Marketing Brochure: Category Management – Assortment Optimization

Create a compelling a 1-page marketing brochure around a service that allows Brill International retailers to optimize their product assortments in their stores. The brochure must be fun, very professionally done, clean, and exciting to want possible clients to want to pick up. See word file for content details. The Brill Worldwide Partners red and white colors should be used. Also, include relevant photos to liven up the brochure.

Target Market(s)

Brill Toolworks Retailers in Different Parts of the World

Industry/Entity Type

Retail

Font styles to use
Sans Serif

Requirements
Must have
• See Word file. Add some really good photos relevant to retail.
• Red and White Colors would be good to match Brill Worldwide Partners logo
• Also, should look like a 'global' service. Maybe add a worldly look to it.
Nice to have
• See World file
Should not have
• N/A

```html
<!DOCTYPE html>
<html lang="en">
<head>
<meta charset="utf-8">
<title>Category Management – Assortment Optimization</title>
<link rel="stylesheet" href="https://fonts.googleapis.com/css2?family=Anton&family=Open+Sans:wght@400;600&family=Ubuntu:wght@500;700&display=swap">
<style>
  :root {
    --brand-red: #e31b37;
    --ink: #1c1c1c;
    --charcoal: #231f20;
    --panel-grey: #ececec;
    --paper: #ffffff;
    --stage: #a6a6a6;
    --photo-deep: #0d2a5c;
    --photo-mid: #2a6bc0;
    --photo-glow: #8fc4f2;
  }
  * { box-sizing: border-box; margin: 0; padding: 0; }
  html, body { width: 1200px; height: 1200px; overflow: hidden; }
  body {
    background: var(--stage);
    font-family: "Open Sans", Arial, sans-serif;
    color: var(--ink);
  }
  .brochure {
    position: absolute;
    left: 190px; top: 25px;
    width: 820px; height: 1150px;
    background: var(--paper);
    display: flex; flex-direction: column;
  }
  .hero-photo {
    height: 375px;
    background:
      radial-gradient(ellipse at 55% 55%, var(--photo-glow) 0%, rgba(143,196,242,0) 45%),
      linear-gradient(160deg, var(--photo-deep) 0%, var(--photo-mid) 55%, var(--photo-deep) 100%);
  }
  .title-band {
    height: 158px;
    background: var(--brand-red);
    display: flex; flex-direction: column; align-items: center; justify-content: center;
    font-family: "Anton", Impact, sans-serif;
    font-weight: 400;
    line-height: 1;
    text-transform: uppercase;
  }
  .title-band .title-main { color: #000; font-size: 64px; letter-spacing: 6px; font-weight: 400; }
  .title-band .title-sub { color: var(--paper); font-size: 60px; margin-top: 6px; letter-spacing: 5px; font-weight: 400; }
  .content {
    height: 560px;
    display: flex;
  }
  .col-left {
    width: 410px;
    background: var(--panel-grey);
    padding: 18px 12px 0 33px;
  }
  .col-right {
    width: 410px;
    padding: 16px 26px 0 14px;
  }
  .section-title {
    font-family: "Ubuntu", sans-serif;
    font-weight: 700;
    color: var(--brand-red);
    font-size: 21px;
    line-height: 1.25;
  }
  .intro-title { margin-bottom: 10px; }
  .body-copy {
    font-size: 11.4px;
    line-height: 1.42;
    text-align: justify;
    margin-bottom: 12px;
  }
  .approach-title { margin-top: 20px; margin-bottom: 6px; }
  .tick-list { list-style: none; }
  .col-left .tick-list { padding-right: 26px; }
  .tick-list li {
    position: relative;
    padding-left: 18px;
    font-size: 13.2px;
    line-height: 1.35;
    margin-bottom: 8px;
  }
  .tick-list li::before {
    content: "";
    position: absolute; left: 0; top: 4px;
    width: 11px; height: 11px; border-radius: 50%;
    background: var(--brand-red);
  }
  .tick-list li::after {
    content: "";
    position: absolute; left: 3.5px; top: 6px;
    width: 3px; height: 5px;
    border: solid var(--paper);
    border-width: 0 1.6px 1.6px 0;
    transform: rotate(45deg);
  }
  .col-right .section-title { margin-bottom: 6px; }
  .col-right .tick-list li { padding-right: 4px; }
  .about-box {
    margin-top: 12px;
    margin-left: -6px;
    background: var(--charcoal);
    color: var(--paper);
    padding: 12px 14px 14px 14px;
    width: 378px;
  }
  .about-box .section-title { margin-bottom: 6px; }
  .about-box p { font-size: 11.4px; line-height: 1.4; }
  .brand-name {
    margin-top: 48px;
    padding-left: 14px;
    font-family: "Ubuntu", sans-serif;
    font-weight: 700;
    font-size: 26px;
    line-height: 1.1;
    color: var(--ink);
  }
  .footer-bar {
    height: 57px;
    background: var(--charcoal);
    color: var(--paper);
    display: flex; align-items: center; justify-content: center;
    font-size: 15px;
    letter-spacing: 1.6px;
  }
</style>
</head>
<body>
  <article class="brochure">
    <div class="hero-photo" role="img" aria-label="Photo of an open hand beneath glowing blue holographic sales charts, bar graphs and pie charts"></div>

    <header class="title-band">
      <h1 class="title-main">Category Management</h1>
      <h2 class="title-sub">Assortment Optimization</h2>
    </header>

    <section class="content">
      <div class="col-left">
        <h3 class="section-title intro-title">Satisfying Customers with<br>Data-Driven, Informed Decisions</h3>
        <p class="body-copy">It takes a strong category strategy to drive sales growth. With changes in consumer demands and product introductions constantly making their way into the market, it's not easy to optimize product selection toward maximizing market share and wider profit margins. To do so, companies need to quickly and effectively deploy well-established and nimble methodologies that refine and enhance category assortment and retail space decisions.</p>
        <p class="body-copy">Brill Worldwide Partners category management's monthly services provides your business industry expertise, functional richness, and retail data analytics know-how to drive more profitable and productive product assortments. We speak analytics. In doing so, we synthesize raw data, assess it, and covert it into practical, measured solutions to help your business grow.</p>

        <h3 class="section-title approach-title">Our Service Approach:</h3>
        <ul class="tick-list">
          <li>Understand your long-term vision, market and assortment objectives</li>
          <li>Assess the current state of affairs to your categories</li>
          <li>Obtain store level raw data one category at a time</li>
          <li>Covert raw data into powerful insights about category performance, opportunities, potential impact, and goal setting</li>
          <li>Implement recommendations, track results, and further advise</li>
        </ul>
      </div>

      <div class="col-right">
        <h3 class="section-title">Return on Investment:</h3>
        <ul class="tick-list">
          <li>Increased profitability and turnover</li>
          <li>Simplify assortments and planograms create a more consumer-friendly shopping experience</li>
          <li>Attack over-SKU'd categories and less duplication</li>
          <li>Fact-based analytics with collaborative market insights</li>
          <li>Reduce wasteful spending and to help brands help retailers compete more effectively</li>
          <li>Acquired processes are safeguarded for the long-term</li>
          <li>The customer remains at the heart of decision making</li>
        </ul>

        <div class="about-box">
          <h3 class="section-title">About Brill Worldwide Partners:</h3>
          <p>Brill Worldwide Partners is a Brill International consulting service that provides training and strategy recommendations based on Brill's 94-year retail industry expertise. Our services drive significant and sustainable performance improvements so you can accomplish your company's most important business objectives</p>
        </div>

        <div class="brand-name">Brill Worldwide Partners</div>
      </div>
    </section>

    <footer class="footer-bar">www.brillworldwidepartners.com</footer>
  </article>
</body>
</html>
```